Business Card

The design you sent was fine. I just need the logo changed on one side. The back needs to have the text "Vell Marrow Group" next to the log and the words "Insight Counsel Strategy" in the middle. The front logo needs to have the "Vell Marrow Advisory" logo attached

Colors

Designer to choose colors to be used in the design.

```html
<!DOCTYPE html>
<html lang="en">
<head>
<meta charset="utf-8">
<title>Vell Marrow Advisory – Business Card</title>
<link rel="stylesheet" href="https://fonts.googleapis.com/css2?family=Open+Sans:wght@400;600;700&display=swap">
<style>
  :root {
    --page-bg: #1e1e1e;
    --card-dark: #161616;
    --pattern-tone: #232323;
    --card-light: #ffffff;
    --card-light-shade: #f1f1f1;
    --ink: #1b1b1b;
    --accent: #1fb0df;
    --white: #ffffff;
  }
  * { box-sizing: border-box; margin: 0; padding: 0; }
  html, body {
    width: 1200px; height: 1021px; overflow: hidden;
    background: var(--page-bg);
    font-family: "Open Sans", Arial, sans-serif;
  }
  .canvas { position: relative; width: 1200px; height: 1021px; }
  .card {
    position: absolute; left: 275px; width: 650px; height: 372px;
    box-shadow: 0 10px 30px rgba(0,0,0,.45);
  }
  .card-back { top: 90px; background: var(--card-dark); overflow: hidden; }
  .card-back .pattern-fill {
    position: absolute; inset: 0;
    background: radial-gradient(ellipse at center, var(--pattern-tone), var(--card-dark));
  }
  .card-back .brand-block {
    position: absolute; inset: 0;
    display: flex; flex-direction: column; align-items: center; justify-content: center;
    color: var(--white); text-align: center;
  }
  .card-back .group-name { font-size: 38px; font-weight: 600; letter-spacing: 0.5px; line-height: 1.1; }
  .card-back .values-line { margin-top: 4px; font-size: 18px; font-weight: 400; letter-spacing: 1.6px; }
  .card-front {
    top: 540px;
    background: linear-gradient(180deg, var(--card-light) 55%, var(--card-light-shade));
    color: var(--ink);
  }
  .logo-lockup { position: absolute; left: 40px; top: 36px; }
  .logo-row { display: flex; align-items: center; gap: 12px; }
  .logo-dot { width: 46px; height: 46px; border-radius: 50%; border: 5px solid var(--accent); }
  .logo-name { font-size: 26px; font-weight: 600; color: var(--ink); line-height: 1.1; }
  .logo-tagline {
    margin-top: 6px; margin-left: 58px;
    font-size: 8px; font-weight: 600; letter-spacing: 0.2px; color: var(--ink);
  }
  .contact-block {
    position: absolute; left: 40px; bottom: 40px;
    font-size: 17px; line-height: 1.35; color: var(--ink);
  }
  .contact-block .address { margin-bottom: 4px; }
  .contact-line { display: flex; align-items: center; gap: 8px; }
  .contact-line svg { width: 15px; height: 15px; flex: none; }
  .person-block { position: absolute; right: 48px; top: 172px; text-align: right; }
  .person-name { font-size: 26px; font-weight: 600; color: var(--accent); line-height: 1.15; }
  .person-title { font-size: 19px; color: var(--ink); }
</style>
</head>
<body>
<main class="canvas">

  <section class="card card-back" aria-label="Card back">
    <div class="pattern-fill" role="img" aria-label="Repeating tone-on-tone pattern of small framed eye motifs"></div>
    <div class="brand-block">
      <p class="group-name">Vell Marrow Group</p>
      <p class="values-line">Insight Counsel Strategy</p>
    </div>
  </section>

  <section class="card card-front" aria-label="Card front">
    <div class="logo-lockup">
      <div class="logo-row">
        <span class="logo-dot" aria-hidden="true"></span>
        <span class="logo-name">Vell Marrow Advisory</span>
      </div>
      <p class="logo-tagline">Considered Thinking delivering Lasting Results</p>
    </div>

    <div class="contact-block">
      <p class="address">240 Harbor Lane, Suite 310<br>Brightwater, Florida, 33190</p>
      <p class="contact-line">
        <svg viewBox="0 0 16 16" aria-hidden="true"><path fill="#1fb0df" d="M3.6 1.5l2.2 2.8-1.3 1.6c.9 2 2.6 3.7 4.6 4.6l1.6-1.3 2.8 2.2-1.4 2.1C6.8 13.6 2.4 9.2 1.5 3z"/></svg>
        (555) 214-0387
      </p>
      <p class="contact-line">
        <svg viewBox="0 0 16 16" aria-hidden="true"><rect x="1" y="3" width="14" height="10" fill="none" stroke="#1fb0df" stroke-width="1.5"/><path d="M1 3l7 6 7-6" fill="none" stroke="#1fb0df" stroke-width="1.5"/></svg>
        daniel@vellmarrow-advisory.com
      </p>
      <p class="contact-line">
        <svg viewBox="0 0 16 16" aria-hidden="true"><g fill="none" stroke="#1fb0df" stroke-width="1.2"><circle cx="8" cy="8" r="6.5"/><ellipse cx="8" cy="8" rx="3" ry="6.5"/><path d="M1.5 8h13M2.5 4.8h11M2.5 11.2h11"/></g></svg>
        www.vellmarrow-advisory.com
      </p>
    </div>

    <div class="person-block">
      <p class="person-name">Daniel Carter</p>
      <p class="person-title">President</p>
    </div>
  </section>

</main>
</body>
</html>
```